Animated Banner Design for a snacking company

We need a set of banner design to to fit the all the google ad words designs. The banners should be animated and static. Our product has it colors identity that should be used with characters. it should match a movie that explains the product.

The product is subscription serivce that target individual with a healthy lifestyle.

Please visit tarvo.qelmandi.com and watch the movie on you tube.

Target Market(s)

Males and Females Age from 18 to 38

Industry/Entity Type

Food Store

Font styles to use
Other font styles liked:
• Lato

Colors
3176b5
f37122
5c5c5c

Requirements
Must have
• color scheme to match the video and color codes.
• animation

```html
<!DOCTYPE html>
<html lang="en">
<head>
<meta charset="utf-8">
<title>Tarvo – Weekly Nut Mix Banner Set</title>
<link rel="stylesheet" href="https://fonts.googleapis.com/css2?family=Arimo:wght@400;700&display=swap">
<style>
:root{
  --page:#ffffff;
  --label:#4a4a4a;
  --header-blue:#7b93c6;
  --panel-dark:#3a3a48;
  --ribbon:#fdd08c;
  --ribbon-text:#3a3a48;
  --illus-teal:#bfe0e0;
  --illus-nut:#d9a86a;
  --logo-grey:#e1e1e1;
  --footer-sage:#c8d4cc;
  --swoosh-gold:#c9b36b;
  --cta-top:#f7923f;
  --cta-bottom:#e2611a;
  --cta-icon:#8a3a10;
  --bullet:#bcd95a;
  --white:#ffffff;
  --frame:#8a8a8a;
}
*{box-sizing:border-box;margin:0;padding:0}
html,body{width:1200px;height:1200px;overflow:hidden;background:var(--page)}
body{font-family:"Arimo",Arial,sans-serif}
.sheet{position:absolute;left:6px;top:2px;width:850px;height:860px;transform:scale(1.395);transform-origin:0 0}
.set-label{position:absolute;font-size:17px;color:var(--label);font-weight:400}

.banner{position:absolute;overflow:hidden;border:1px solid var(--frame);background:var(--logo-grey)}
.banner > *{position:absolute}
.headline{color:var(--white);font-weight:700;text-transform:uppercase;background:var(--header-blue)}
.ribbon{background:var(--ribbon);color:var(--ribbon-text);text-align:center;font-size:13px;line-height:14px;white-space:nowrap;
  clip-path:polygon(0 0,100% 0,100% 100%,50% 84%,0 100%)}
.illustration{background:radial-gradient(circle at 35% 45%,var(--illus-nut) 0 22%,transparent 23%),
  linear-gradient(160deg,var(--illus-teal),#a9d3d6)}
.dark-panel{background:var(--panel-dark)}
.fact{color:var(--white);font-weight:700;font-size:13px;line-height:15.5px}
.benefits{list-style:none;color:var(--white);font-weight:700;font-size:14px;line-height:19px}
.benefits li{position:relative;padding-left:18px}
.benefits li::before{content:"";position:absolute;left:2px;top:4px;border-left:9px solid var(--bullet);
  border-top:5.5px solid transparent;border-bottom:5.5px solid transparent}
.brand{color:var(--panel-dark);font-weight:700;letter-spacing:.5px;line-height:1}
.cta{display:flex;align-items:center;justify-content:space-between;padding:0 4px 0 9px;border-radius:3px;
  background:linear-gradient(var(--cta-top),var(--cta-bottom));color:var(--white);font-size:13px;font-weight:700;
  box-shadow:0 1px 2px rgba(0,0,0,.3)}
.cta-icon{width:24px;height:24px;border-radius:50%;background:var(--cta-icon);border:2px solid #f6a060;position:relative}
.cta-icon::after{content:"";position:absolute;left:8px;top:5px;border-left:8px solid var(--white);
  border-top:5px solid transparent;border-bottom:5px solid transparent}
.swoosh{display:block}

/* leaderboard 727 x 88 */
.banner--leader{width:727px;height:88px;left:113px}
.banner--leader .headline{left:0;top:0;width:215px;height:88px;padding:7px 50px 0 10px;font-size:15px;line-height:18px}
.banner--leader .ribbon{left:168px;top:0;width:60px;height:88px;padding-top:12px;font-size:12px}
.banner--leader .illustration{left:228px;top:0;width:178px;height:88px}
.banner--leader .swoosh{left:400px;top:0;width:220px;height:88px}
.banner--leader .fact{left:425px;top:9px;width:135px;font-size:12.5px;line-height:14px}
.banner--leader .benefits{left:425px;top:7px}
.banner--leader .brand{left:603px;top:7px;font-size:32px}
.banner--leader .footer{left:585px;top:44px;width:142px;height:44px;background:var(--footer-sage)}
.banner--leader .cta{left:592px;top:50px;width:127px;height:32px}

/* medium rectangle 300 x 250 */
.banner--rect{width:300px;height:250px;left:13px}
.banner--rect .headline{left:0;top:0;width:300px;height:62px;padding:6px 90px 0 17px;font-size:15px;line-height:16px}
.banner--rect .dark-panel{left:142px;top:62px;width:158px;height:130px}
.banner--rect .illustration{left:0;top:62px;width:142px;height:130px}
.banner--rect .ribbon{left:208px;top:0;width:82px;height:80px;padding-top:17px}
.banner--rect .fact{left:153px;top:96px;width:128px}
.banner--rect .benefits{left:157px;top:95px}
.banner--rect .swoosh{left:0;top:150px;width:300px;height:100px}
.banner--rect .brand{left:175px;top:206px;font-size:33px}
.banner--rect .cta{left:12px;top:205px;width:128px;height:34px}

/* skyscraper 160 x 600 */
.banner--sky{width:160px;height:600px;top:210px}
.banner--sky .headline{left:0;top:0;width:160px;height:148px;padding:11px 22px 0;text-align:center;font-size:19px;line-height:19px}
.banner--sky .dark-panel{left:0;top:148px;width:160px;height:190px}
.banner--sky .ribbon{left:40px;top:142px;width:82px;height:86px;padding-top:17px}
.banner--sky .illustration{left:0;top:330px;width:160px;height:150px}
.banner--sky .fact{left:18px;top:244px;width:124px;text-align:center;font-size:12.5px;line-height:14px}
.banner--sky .benefits{left:20px;top:242px}
.banner--sky .swoosh{left:0;top:455px;width:160px;height:145px}
.banner--sky .brand{left:0;width:160px;text-align:center;top:502px;font-size:34px}
.banner--sky .cta{left:16px;top:556px;width:128px;height:32px}
</style>
</head>
<body>
<main class="sheet">

  <span class="set-label" style="left:25px;top:42px">Animatic</span>
  <span class="set-label" style="left:25px;top:131px">Static</span>

  <!-- Leaderboard, animated -->
  <section class="banner banner--leader" style="top:10px">
    <h2 class="headline">Your weekly mix of nuts for a healthy lifestyle</h2>
    <div class="ribbon">What<br>Makes<br>Great Nuts!</div>
    <div class="illustration" role="img" aria-label="Mixed nuts beside a hand holding a phone showing the order app"></div>
    <svg class="swoosh" viewBox="0 0 220 88" aria-hidden="true">
      <path d="M0 0H175Q205 44 185 88H0Z" fill="var(--panel-dark)"/>
      <path d="M175 0Q205 44 185 88" fill="none" stroke="var(--swoosh-gold)" stroke-width="5"/>
    </svg>
    <p class="fact">Did You Know that Eating A Handfull Of Nuts A Day Can Make You Live Longer?</p>
    <div class="footer"></div>
    <span class="brand">tarvo</span>
    <a class="cta">CLICK HERE<span class="cta-icon"></span></a>
  </section>

  <!-- Leaderboard, static -->
  <section class="banner banner--leader" style="top:104px">
    <h2 class="headline">Your weekly mix of nuts for a healthy lifestyle</h2>
    <div class="ribbon">What<br>Makes<br>Great Nuts!</div>
    <div class="illustration" role="img" aria-label="Mixed nuts beside a hand holding a phone showing the order app"></div>
    <svg class="swoosh" viewBox="0 0 220 88" aria-hidden="true">
      <path d="M0 0H175Q205 44 185 88H0Z" fill="var(--panel-dark)"/>
      <path d="M175 0Q205 44 185 88" fill="none" stroke="var(--swoosh-gold)" stroke-width="5"/>
    </svg>
    <ul class="benefits"><li>PROTEIN</li><li>RAW ORGANIC</li><li>FAT BLOCKER</li><li>PROBIOTIC</li></ul>
    <div class="footer"></div>
    <span class="brand">tarvo</span>
    <a class="cta">CLICK HERE<span class="cta-icon"></span></a>
  </section>

  <span class="set-label" style="left:330px;top:327px">Animatic</span>
  <span class="set-label" style="left:328px;top:580px">Static</span>

  <!-- Medium rectangle, animated -->
  <section class="banner banner--rect" style="top:209px">
    <h2 class="headline">Your weekly mix of nuts for a healthy lifestyle</h2>
    <div class="dark-panel"></div>
    <div class="illustration" role="img" aria-label="Mixed nuts beside a hand holding a phone showing the order app"></div>
    <div class="ribbon">What<br>Makes<br>Great Nuts!</div>
    <p class="fact">Did You Know that Eating A Handfull Of Nuts A Day Can Make You Live Longer?</p>
    <svg class="swoosh" viewBox="0 0 300 100" aria-hidden="true">
      <path d="M0 22Q120 50 300 38V100H0Z" fill="var(--logo-grey)"/>
      <path d="M0 22Q120 50 155 49V100H0Z" fill="var(--footer-sage)"/>
      <path d="M0 22Q120 50 300 38" fill="none" stroke="var(--swoosh-gold)" stroke-width="5"/>
    </svg>
    <span class="brand">tarvo</span>
    <a class="cta">CLICK HERE<span class="cta-icon"></span></a>
  </section>

  <!-- Medium rectangle, static -->
  <section class="banner banner--rect" style="top:470px">
    <h2 class="headline">Your weekly mix of nuts for a healthy lifestyle</h2>
    <div class="dark-panel"></div>
    <div class="illustration" role="img" aria-label="Mixed nuts beside a hand holding a phone showing the order app"></div>
    <div class="ribbon">What<br>Makes<br>Great Nuts!</div>
    <ul class="benefits"><li>PROTEIN</li><li>RAW ORGANIC</li><li>FAT BLOCKER</li><li>PROBIOTIC</li></ul>
    <svg class="swoosh" viewBox="0 0 300 100" aria-hidden="true">
      <path d="M0 22Q120 50 300 38V100H0Z" fill="var(--logo-grey)"/>
      <path d="M0 22Q120 50 155 49V100H0Z" fill="var(--footer-sage)"/>
      <path d="M0 22Q120 50 300 38" fill="none" stroke="var(--swoosh-gold)" stroke-width="5"/>
    </svg>
    <span class="brand">tarvo</span>
    <a class="cta">CLICK HERE<span class="cta-icon"></span></a>
  </section>

  <!-- Skyscraper, animated -->
  <section class="banner banner--sky" style="left:513px">
    <h2 class="headline">Your weekly mix of nuts for a healthy lifestyle</h2>
    <div class="dark-panel"></div>
    <div class="illustration" role="img" aria-label="Mixed nuts beside a hand holding a phone showing the order app"></div>
    <div class="ribbon">What<br>Makes<br>Great Nuts!</div>
    <p class="fact">Did You Know that Eating A Handfull Of Nuts A Day Can Make You Live Longer?</p>
    <svg class="swoosh" viewBox="0 0 160 145" aria-hidden="true">
      <path d="M0 15Q60 45 160 24V145H0Z" fill="var(--logo-grey)"/>
      <rect x="0" y="90" width="160" height="55" fill="var(--footer-sage)"/>
      <path d="M0 15Q60 45 160 24" fill="none" stroke="var(--swoosh-gold)" stroke-width="5"/>
    </svg>
    <span class="brand">tarvo</span>
    <a class="cta">CLICK HERE<span class="cta-icon"></span></a>
  </section>

  <!-- Skyscraper, static -->
  <section class="banner banner--sky" style="left:680px">
    <h2 class="headline">Your weekly mix of nuts for a healthy lifestyle</h2>
    <div class="dark-panel"></div>
    <div class="illustration" role="img" aria-label="Mixed nuts beside a hand holding a phone showing the order app"></div>
    <div class="ribbon">What<br>Makes<br>Great Nuts!</div>
    <ul class="benefits"><li>PROTEIN</li><li>RAW ORGANIC</li><li>FAT BLOCKER</li><li>PROBIOTIC</li></ul>
    <svg class="swoosh" viewBox="0 0 160 145" aria-hidden="true">
      <path d="M0 15Q60 45 160 24V145H0Z" fill="var(--logo-grey)"/>
      <rect x="0" y="90" width="160" height="55" fill="var(--footer-sage)"/>
      <path d="M0 15Q60 45 160 24" fill="none" stroke="var(--swoosh-gold)" stroke-width="5"/>
    </svg>
    <span class="brand">tarvo</span>
    <a class="cta">CLICK HERE<span class="cta-icon"></span></a>
  </section>

  <span class="set-label" style="left:565px;top:819px">Animatic</span>
  <span class="set-label" style="left:734px;top:819px">Static</span>

</main>
</body>
</html>
```